Case Study - Ulvar case study layout

We would like to convert the example into flyer-like layout for our biotech consultancy. Attached rough concept contains text and rough layout, but looking for help making this flow. I can provide the logo etc in additional formats as required. The design should convey experience and professionalism.

Target Market(s)

Start-up biotech companies

Industry/Entity Type

Biotechnology

Font styles to use
Sans Serif

Colors
0054AA
0677BA
7BADD7
CADEEF
E8F1F8

Requirements
Must have
• professional look and feel, legible text
Nice to have
• N/A
Should not have
• N/A

```html
<!DOCTYPE html>
<html lang="en">
<head>
<meta charset="utf-8">
<title>Ulvar Case Study – Building an Early-Stage Diagnostics Company</title>
<link rel="stylesheet" href="https://fonts.googleapis.com/css2?family=Poppins:wght@400;500;600;700;800&display=swap">
<style>
  :root{
    --navy:#0054AA;
    --blue:#0677BA;
    --sky:#7BADD7;
    --pale:#CADEEF;
    --mist:#E8F1F8;
    --ink:#1d1d1d;
    --charcoal:#2b2b2d;
    --grey-panel:#ececec;
    --backdrop:#c8c8ca;
    --white:#ffffff;
  }
  *{box-sizing:border-box;margin:0;padding:0}
  html,body{width:1200px;height:848px;overflow:hidden;background:var(--backdrop);font-family:"Poppins",Arial,sans-serif;color:var(--ink)}
  .page{position:absolute;top:93px;width:512px;height:662px;background:var(--white);overflow:hidden}
  .page--front{left:70px}
  .page--back{left:618px}
  .abs{position:absolute}

  /* brand */
  .brand{left:30px;top:40px;width:130px;display:flex;align-items:center;gap:6px}
  .brand__dot{width:12px;height:12px;border-radius:50%;background:var(--navy);flex:none}
  .brand__name{font-weight:600;font-size:11.5px;line-height:1.1;color:var(--navy)}

  .tag{left:30px;top:106px;height:18px;padding:0 6px;background:var(--navy);color:var(--white);font-weight:700;font-size:11.5px;line-height:18px;border-radius:2px}
  .title{left:29px;top:124px;line-height:0.95;font-weight:800}
  .title__dark{font-size:24px;color:var(--ink);display:block;letter-spacing:.3px}
  .title__blue{font-size:33.5px;color:var(--navy);display:block;letter-spacing:.3px}

  .hero-photo{left:266px;top:0;width:246px;height:240px}

  /* intro band */
  .intro{left:0;top:239px;width:512px;height:122px;background:var(--charcoal);color:var(--white);padding:12px 30px 0 31px}
  .intro h2{font-weight:700;font-size:17px;line-height:1;margin-bottom:9px}
  .intro p{font-size:6.3px;line-height:1.3;margin-bottom:4px;color:#e6e6e6}

  .section-head{height:24px;padding:0 6px;background:var(--navy);color:var(--white);font-weight:700;font-size:15px;line-height:24px;box-shadow:3px 3px 0 #0f2a4a;white-space:nowrap}
  .body-copy{font-size:6.3px;line-height:1.3;color:#2b2b2b}

  .callout{background:var(--pale);color:#1b2a3a;text-align:center;display:flex;align-items:center;justify-content:center;box-shadow:3px 3px 0 #b8bfc7}
  .callout__fold{position:absolute;right:0;bottom:0;width:0;height:0;border-left:18px solid transparent;border-bottom:18px solid var(--backdrop)}
  .callout__fold::after{content:"";position:absolute;left:-18px;top:0;width:18px;height:18px;background:linear-gradient(315deg,transparent 50%,var(--sky) 50%)}

  /* timeline */
  .timeline{left:30px;top:461px;width:452px;height:140px}
  .stage-col{position:absolute;top:24px;width:113px;height:99px;padding:30px 10px 0 10px;font-size:6.2px;line-height:1.25;color:#333}
  .stage-col:nth-child(odd){background:var(--pale)}
  .stage-col:nth-child(even){background:var(--grey-panel)}
  .stage-label{position:absolute;top:12px;color:var(--white);font-weight:600;font-size:7.3px;line-height:1.2}

  .footer-bar{left:30px;top:607px;width:452px;height:26px;background:#262626;color:var(--white);display:flex;align-items:center;font-size:10.5px}
  .footer-bar__cell{flex:1;display:flex;align-items:center;justify-content:center;gap:5px;border-right:1px solid #555;height:16px}
  .footer-bar__cell:last-child{border-right:none}
  .social{display:flex;gap:2px;margin-left:3px}
  .social i{width:8px;height:8px;border-radius:50%;background:var(--blue);display:block}

  /* back page */
  .top-band{left:0;top:0;width:512px;height:178px;background:var(--navy)}
  .top-photo{left:0;top:0;width:250px;height:178px}
  .top-band h2{position:absolute;left:264px;top:33px;color:var(--white);font-weight:700;font-size:16px;line-height:1.05}
  .top-band p{position:absolute;left:264px;top:78px;width:212px;color:#e3ecf6;font-size:6.3px;line-height:1.3}

  .photo-frame{box-shadow:3px 3px 0 var(--navy)}
  .conclusion{left:30px;top:464px;width:216px;height:74px;background:var(--grey-panel)}
  .conclusion__tab{position:absolute;left:2px;top:2px;height:15px;width:96px;background:var(--navy);color:var(--white);font-weight:700;font-size:10px;line-height:15px;padding-left:10px;clip-path:polygon(0 0,100% 0,88% 100%,0 100%)}
  .about{left:30px;top:547px;width:450px;height:48px;background:var(--pale);padding:8px 14px;font-size:6.4px;line-height:1.3;color:#222}
  .about strong{font-weight:700;font-size:7.2px}
</style>
</head>
<body>

<!-- FRONT PAGE -->
<section class="page page--front">
  <div class="abs brand"><span class="brand__dot"></span><span class="brand__name">OMEC ULVAR GROUP</span></div>

  <div class="abs tag">OUG CASE STUDY</div>
  <h1 class="abs title">
    <span class="title__dark">BUILDING AN</span>
    <span class="title__dark">EARLY-STAGE</span>
    <span class="title__blue">DIAGNOSTICS</span>
    <span class="title__blue">COMPANY</span>
  </h1>

  <svg class="abs hero-photo" viewBox="0 0 246 240" role="img" aria-label="Photo: two colleagues smiling at a laptop in a bright office">
    <defs>
      <linearGradient id="officeTone" x1="0" y1="0" x2="1" y2="1">
        <stop offset="0" stop-color="#d8c7b0"/>
        <stop offset=".5" stop-color="#a9876a"/>
        <stop offset="1" stop-color="#5c4a3d"/>
      </linearGradient>
    </defs>
    <path d="M70 0 H246 V240 H110 C40 215 5 160 5 110 C5 60 30 20 70 0 Z" fill="url(#officeTone)"/>
    <path d="M60 0 C20 25 -5 70 -5 115 C-5 170 35 222 100 240" fill="none" stroke="var(--navy)" stroke-width="7"/>
  </svg>

  <div class="abs intro">
    <h2>INTRODUCTION</h2>
    <p>Omec Ulvar Group provides a full range of experience and services designed to preserve capital and accelerate growth of early-stage companies looking to convert technologies into commercial products.</p>
    <p>This case study examines how OUG has provided experience to a partner in the cancer diagnostics field through our Ulvar Plan. This partner recently organized as a university spin-out company using initial seed funding but needed to build out a comprehensive strategy to attract the next round of investment for developing the initial set of products.</p>
    <p>By providing complementary experiences, OUG has been able to verify the product's intended use as a clear unmet clinical need, establish a workable reimbursement plan, develop a key opinion leader (KOL) network and secure funding for the initial product concept through validation.</p>
  </div>

  <div class="abs section-head" style="left:30px;top:373px;width:220px">EARLY PRODUCT STRATEGY</div>
  <p class="abs body-copy" style="left:31px;top:404px;width:280px">Initial interactions revolved around defining and creating requirements for the initial novel diagnostic technology, which promises to change the treatment and management of a common form of metastatic cancer. To assess the best developmental and commercial path, OUG was engaged to map out the following product areas.</p>

  <div class="abs callout" style="left:320px;top:369px;width:162px;height:82px;padding:0 14px;font-size:8.6px;line-height:1.2">
    The Ulvar Plan approaches strategic planning with the end-goal as the starting point, producing a proven, tailored, and streamlined path to commercial success
    <span class="callout__fold"></span>
  </div>

  <div class="abs timeline">
    <div class="stage-col" style="left:0"><br>Provisional Patent<br>Investor Engagement<br>Licensing agreements<br>Market opportunity</div>
    <div class="stage-col" style="left:113px"><br>Voice of customer User requirements Business / Revenue model Competitive landscape Initial commercial plan Quality and Regulatory Plan</div>
    <div class="stage-col" style="left:226px"><br>Feasibility data<br>Co-development partner<br>SAB / KOL Recruitment<br>Quality system execution<br>Regulatory Pre-submissions<br>Supply chain plan</div>
    <div class="stage-col" style="left:339px"><br>Product verification plan<br>Product roadmap<br>Commercial launch plan<br>Pitch Deck Fundraising</div>

    <svg class="abs" style="left:0;top:0" width="452" height="140" viewBox="0 0 452 140" aria-hidden="true">
      <rect x="0" y="14" width="452" height="24" fill="var(--navy)"/>
      <g fill="var(--navy)" stroke="var(--white)" stroke-width="0">
        <polygon points="88,0 116,26 88,52 88,38 0,38 0,14 88,14"/>
        <polygon points="201,0 229,26 201,52 201,38 116,38 116,14 201,14"/>
        <polygon points="314,0 342,26 314,52 314,38 229,38 229,14 314,14"/>
        <polygon points="427,0 452,26 427,52 427,38 342,38 342,14 427,14"/>
      </g>
      <line x1="0" y1="124" x2="452" y2="124" stroke="var(--navy)" stroke-width="2"/>
      <g fill="var(--navy)">
        <circle cx="56" cy="124" r="14"/><circle cx="169" cy="124" r="14"/>
        <circle cx="282" cy="124" r="14"/><circle cx="395" cy="124" r="14"/>
      </g>
      <g fill="none" stroke="var(--white)" stroke-width="1.6">
        <circle cx="56" cy="124" r="5"/><path d="M56 115v3M56 130v3M47 124h3M62 124h3"/>
        <path d="M162 126h14l-3 5h-8z M169 117v9"/><circle cx="169" cy="117" r="2"/>
        <circle cx="282" cy="122" r="5"/><path d="M279 129h6M280 132h4"/>
        <path d="M389 122l6-4 6 4v7h-12z M395 118v11"/>
      </g>
    </svg>
    <div class="stage-label" style="left:10px;top:6px">Technology and<br>Intellectual Property</div>
    <div class="stage-label" style="left:124px;top:15px">Product Definition</div>
    <div class="stage-label" style="left:237px;top:15px">Proof of Concept</div>
    <div class="stage-label" style="left:350px;top:6px">Early Product<br>Development</div>
  </div>

  <div class="abs footer-bar">
    <div class="footer-bar__cell">✉ info@omeculvar.com</div>
    <div class="footer-bar__cell">◍ www.omeculvar.com</div>
    <div class="footer-bar__cell">Follow us on <span class="social"><i></i><i></i><i></i><i></i></span></div>
  </div>
</section>

<!-- BACK PAGE -->
<section class="page page--back">
  <div class="abs top-band">
    <div class="abs top-photo" role="img" aria-label="Photo: two businessmen reviewing a chart at a meeting table" style="background:linear-gradient(120deg,#1f3656 0%,#4e6b8f 45%,#0f3f78 100%)"></div>
    <h2>UNMET NEED AND<br>INTENDED USE</h2>
    <p>It is common for a technology or potential diagnostic device to have multiple potential applications. The team at OUG assessed the core capabilities and growth potential of the partner's technology and mapped the potential applications against current medical guidelines and practices, identifying specific cancers types appropriate for targeting. By combining these findings with the customer's internal technical data, the initial products were identified and a roadmap for future product innovations was built to guide short and long-term strategies.</p>
  </div>

  <div class="abs section-head" style="left:30px;top:195px;width:208px">COMMERCIAL PLANNING</div>
  <div class="abs body-copy" style="left:30px;top:227px;width:214px">
    <p style="margin-bottom:5px">As part of the initial execution against the roadmap, the team at OUG worked with the partner to build a persona for the members of the KOL network. While the initial goal of the network was to provide feedback and clinical research support, the team at OUG also helped the partner identify longer-term goals such as data support for regulatory filings and reimbursement strategy an ideal KOL could help support.</p>
    <p>This allowed OUG to identify and engage a set of KOLs that would be able to support the long-term product development and commercialization activities for the partner, simplifying and reducing the time and resource investment normally associated with assembling these networks.</p>
  </div>

  <div class="abs callout" style="left:264px;top:202px;width:218px;height:105px;padding:0 16px;font-size:10.4px;line-height:1.25">
    A strategic,<br>well-structured KOL network<br>Will proactively jump-start a company's product development and commercialization efforts
    <span class="callout__fold"></span>
  </div>

  <div class="abs section-head" style="left:30px;top:343px;width:172px">COMPANY GROWTH</div>
  <p class="abs body-copy" style="left:30px;top:378px;width:216px">Like many capital-limited early-stage companies, hiring the full-time experienced leadership required for rapid growth was not economically feasible. Fractional leadership by OUG provided ongoing support in areas such quality, regulatory, and commercial where strategy plans are needed for satisfying potential investors. Members of the OUG team also bolstered fund-raising activities through review of investor pitch decks and introductions to new investment opportunities through our collective networks.</p>

  <div class="abs photo-frame" role="img" aria-label="Photo: businesswoman presenting a bar chart beside a laptop in a home office" style="left:266px;top:331px;width:214px;height:195px;background:linear-gradient(135deg,#ece7df 0%,#cfc6ba 55%,#8f8a86 100%)"></div>

  <div class="abs conclusion">
    <div class="conclusion__tab">CONCLUSION</div>
    <p class="body-copy" style="position:absolute;left:10px;top:23px;width:196px">Through engagement and application of OUG's broad range of capabilities, early-stage diagnostic companies may preserve capital and accelerate their product development, organizational growth, and fund-raising activities.</p>
  </div>

  <div class="abs about"><strong>Omec Ulvar Group (OUG) is a group of experienced executives</strong> whose careers have been focused on taking innovative ideas to market by strategically navigating the buildout of best-in-class life science and diagnostic organizations. This experience makes us uniquely equipped to be involved in all aspects of your early-stage company or investment due diligence</div>

  <div class="abs footer-bar" style="top:607px">
    <div class="footer-bar__cell">✉ info@omeculvar.com</div>
    <div class="footer-bar__cell">◍ www.omeculvar.com</div>
    <div class="footer-bar__cell">Follow us on <span class="social"><i></i><i></i><i></i><i></i></span></div>
  </div>
</section>

</body>
</html>
```